INCREASED BUDGET -- Cover Art Template Needed For Record Label

We are an electronic music record label that needs a cover art template for our 2017 releases. The design must be easy to update in Photoshop with different text, colors, or patterns.

The winner will also be asked to design our social media banners for Facebook, Twitter, and SoundCloud, so there's an opportunity to make more money.

Words to describe our sound: sophisticated, forward-thinking, futuristic, modern, emotional

Please make the LA logo the focal point of your design. Feel free to modify our logo as needed. Bonus points for anyone that can find a way to visually represent the word "Lanternfold". Examples of artwork that we found attractive are included to provide inspiration.

You can view our previous releases by clicking on any of the links: https://www.tunevaultshop.example/label/lanternfold-audio/52947/releases

Target Market(s)

Electronic music lovers

Industry/Entity Type

Music Download

Font styles to use
Serif
Decorative
Other font styles liked:
• Aller Display, Aller Light

Requirements
Must have
• Lanternfold Audio record logo
• Name of artist: Rufus Delgarde
• Title: Daybreak / Hold Still (Reworks)
Nice to have
• Tracklist:
• Hold Still (Brantlow Remix)
• Daybreak (Zolvarin Remix)
• Catalog number: 318

```html
<!DOCTYPE html>
<html lang="en">
<head>
<meta charset="utf-8">
<title>Rufus Delgarde – Daybreak / Hold Still (Reworks)</title>
<link href="https://fonts.googleapis.com/css2?family=Michroma&family=Oswald:wght@300;400&display=swap" rel="stylesheet">
<style>
  :root {
    --backdrop: #6e6e6e;
    --backdrop-dark: #4a4a4a;
    --cover-night: #05070c;
    --cover-storm: #1c2a44;
    --cover-violet: #5a4f86;
    --cover-haze: #c9d2dc;
    --title-steel: #d8d8d8;
    --accent-orange: #e2420f;
    --accent-red: #b8321a;
    --text-white: #f2f2f2;
  }
  * { margin: 0; padding: 0; box-sizing: border-box; }
  html, body { width: 1200px; height: 789px; overflow: hidden; }
  body {
    background: radial-gradient(ellipse at 40% 30%, var(--backdrop), var(--backdrop-dark));
    font-family: "Oswald", sans-serif;
  }
  .cover {
    position: absolute;
    left: 250px; top: 45px;
    width: 700px; height: 700px;
    overflow: hidden;
    background: var(--cover-night);
    box-shadow: 0 14px 40px rgba(0,0,0,.45);
  }
  .cover-artwork {
    position: absolute; inset: 0;
    background:
      radial-gradient(circle at 28% 18%, var(--cover-haze) 0%, rgba(201,210,220,.35) 14%, transparent 30%),
      radial-gradient(circle at 12% 42%, var(--cover-violet) 0%, transparent 28%),
      radial-gradient(circle at 62% 45%, #0b0d12 0%, #0b0d12 32%, transparent 46%),
      radial-gradient(circle at 20% 85%, var(--cover-storm) 0%, transparent 45%),
      radial-gradient(circle at 90% 90%, #243656 0%, transparent 40%),
      linear-gradient(160deg, #2b3350 0%, var(--cover-night) 60%, #1a2540 100%);
  }
  .title-block, .label-mark, .credits {
    position: absolute;
    transform: rotate(-19deg);
    transform-origin: left top;
    white-space: nowrap;
  }
  .title-block { left: 40px; top: 300px; }
  .title-main {
    font-family: "Michroma", sans-serif;
    font-size: 60px;
    letter-spacing: 1px;
    color: var(--title-steel);
    text-shadow: 3px 3px 0 #1a1a1a, 0 0 2px #000;
    line-height: 1;
  }
  .title-second {
    font-family: "Michroma", sans-serif;
    font-size: 38px;
    color: var(--accent-orange);
    margin-left: 150px;
    margin-top: 6px;
    line-height: 1;
  }
  .title-edition {
    font-family: "Michroma", sans-serif;
    font-size: 19px;
    color: var(--text-white);
    margin-left: 320px;
    margin-top: 6px;
    line-height: 1;
  }
  .catalog-number {
    font-family: "Michroma", sans-serif;
    font-size: 32px;
    color: var(--accent-red);
    margin-left: 380px;
    margin-top: 10px;
    line-height: 1;
  }
  .label-mark {
    left: 260px; top: 505px;
    display: flex; align-items: center; gap: 12px;
    font-family: "Michroma", sans-serif;
    font-size: 17px;
    color: var(--text-white);
  }
  .label-mark .mark-square {
    width: 20px; height: 20px;
    background: var(--text-white);
  }
  .credits { left: 90px; top: 615px; }
  .tracklist {
    font-size: 15px;
    font-weight: 300;
    color: var(--text-white);
    letter-spacing: .3px;
  }
  .tracklist .divider { color: var(--accent-orange); margin: 0 8px; }
  .artist {
    font-family: "Michroma", sans-serif;
    font-size: 22px;
    letter-spacing: 14px;
    color: var(--text-white);
    margin-top: 12px;
    margin-left: 40px;
    padding-bottom: 6px;
    border-bottom: 1px solid var(--accent-orange);
    display: inline-block;
  }
</style>
</head>
<body>
  <main class="cover">
    <div class="cover-artwork" role="img" aria-label="Stormy violet and blue clouds swirling around a dark vinyl record"></div>

    <div class="title-block">
      <div class="title-main">DAYBREAK</div>
      <div class="title-second">HOLD STILL</div>
      <div class="title-edition">(REWORKS)</div>
      <div class="catalog-number">318</div>
    </div>

    <div class="label-mark">
      <span class="mark-square"></span>
      <span>LANTERNFOLD AUDIO</span>
    </div>

    <div class="credits">
      <p class="tracklist">HOLD STILL (BRANTLOW REMIX)<span class="divider">|</span>DAYBREAK (ZOLVARIN REMIX)</p>
      <p class="artist">RUFUS DELGARDE</p>
    </div>
  </main>
</body>
</html>
```